COMPETITION TITLE:
Premium Skincare Packaging Design for Modern Hydration Beauty Brand
ABOUT THE PROJECT
We are developing a new skincare brand called VELORIQUE.
We are looking for a sophisticated and commercially strong packaging design direction for our initial skincare soft launch.
The brand positioning is:
* modern premium skincare
* hydration-focused
* wellness-oriented
* calming and elegant
* emotionally reassuring
* modern feminine skincare
* premium online beauty brand
The products are designed around hydration, skin comfort and modern skincare rituals.
The brand is inspired by modern hydration and skin wellness for people adapting between warmer and colder climates. The visual direction should therefore feel emotionally warm, comforting and restorative while remaining modern, refined and internationally premium rather than overtly cultural or decorative.
WHAT WE NEED
We are primarily seeking the VISUAL DIRECTION and PACKAGING IDENTITY for one hero product:
LIGHT MOISTURISING DAY CREAM
The winning visual direction will later be adapted across additional products within the range, including:
* Brightening Eye Cream
* Hydrating Mist / Toner
Therefore we are looking for a cohesive skincare brand identity system rather than unrelated individual designs.
IMPORTANT PACKAGING INFORMATION
The product packaging is:
* white plastic pump dispenser bottle
* transparent clear plastic lid
* outer cardboard carton/box
Bottle dimensions:
* diameter: 30mm
* total height including lid: 147mm
* bottle body height: approx. 120mm
* transparent lid height: approx. 27mm
Outer carton dimensions:
* height: 150mm
* width: 40mm x 35mm
IMPORTANT:
The packaging itself is minimalist and lightweight, therefore the LABEL DESIGN and OVERALL BRAND DIRECTION should visually elevate the product and make it feel:
* premium
* substantial
* calming
* elegant
* modern
* trustworthy
* emotionally warm
* intentional
The design should help the packaging feel significantly more premium than standard mass-market skincare.
FILES PROVIDED
We are providing:
* bottle label template
* outer box template
* logo/icon
* packaging dimensions
The supplied logo/icon should be retained conceptually, however designers may professionally refine and recreate/vectorise the artwork where required for packaging consistency and premium presentation.
At this stage we are NOT looking for final technical production artwork.
We are primarily looking for:
* visual direction
* typography
* colour palette
* premium skincare aesthetic
* realistic product mockups
IMPORTANT WEBSITE NOTE
A current website link may be provided for background information only.
Please DO NOT take heavy visual inspiration from the existing website design, as the website itself is expected to evolve in the future alongside the packaging direction.
The packaging design should therefore LEAD the future visual identity of the brand rather than follow the current website styling.
DESIGN STYLE
We are looking for:
* modern premium wellness skincare
* understated luxury
* elegant typography
* emotionally warm but clean branding
* hydration-focused beauty aesthetic
* premium online skincare look
The product should feel:
* calming when held
* emotionally reassuring rather than clinical
* modern wellness rather than minimalist pharmacy
* elegant but human rather than cold luxury
* comforting and restorative rather than cosmetic-only
Subtle texture, tonal layering and sophisticated visual depth are encouraged where appropriate.
Designers are encouraged to create a recognisable and distinctive visual identity rather than generic minimalist skincare packaging.
PLEASE AVOID
* gold luxury clichés
* ornate decorative themes
* floral overload
* influencer-style beauty branding
* overly clinical pharmacy aesthetics
* generic Plindo-style layouts
* packaging that feels cold or sterile
STYLE REFERENCES
Please take inspiration from brands such as:
* Mirova
* Bright Petal
* Coravel
* Grace of Kellmar
We particularly like:
* elegant spacing
* clean premium typography
* calm colour palettes
* subtle luxury
* modern hydration skincare aesthetics
COLOUR DIRECTION
Preferred tones include:
* warm ivory
* soft cream
* muted blush
* sand
* charcoal typography
* subtle deep plum accents
* restrained muted rose-gold accents
Please avoid:
* neon colours
* excessive metallic effects
* harsh black-and-white pharmacy styling
* very dark packaging
IMPORTANT DESIGN NOTE
The slim vertical packaging should feel intentionally elegant and premium rather than small or sample-sized.
The label design should visually elongate and elevate the packaging.
LOGO
An existing logo/icon is provided and should be retained and integrated into the design direction rather than completely redesigned.
DELIVERABLES
We are looking for:
* one fully developed hero product design
* realistic bottle + outer box mockups
* coordinated visual direction suitable for future product extensions
* typography and colour direction
* editable source files
The final approved visual system will later be adapted across additional products within the range.
BRAND NAME
VELORIQUE
OPTIONAL TAGLINE DIRECTION
Climate Adapt Hydration
Updates
Thank you everyone for the submissions so far — there are some very strong directions emerging.
A few important thoughts as the project develops:
We are looking not only for attractive skincare labels, but for a distinctive and recognisable BRAND IDENTITY that could grow with the business over time across future packaging formats including larger cartons, jars and premium skincare packaging.
One area we would particularly encourage designers to explore further is refinement/elevation of the existing logo/icon. We would like to retain the core rose/circle concept, however subtle refinement, balance, geometry, typography pairing and premium presentation are encouraged where appropriate.
The strongest directions for us so far are those that feel:
* emotionally warm rather than clinical
* modern premium wellness rather than generic minimal skincare
* calming and reassuring when viewed or held
* elegant and distinctive rather than trend-driven
* premium without relying on gold luxury clichés
We are especially interested in designs that create a memorable visual identity system rather than simply placing text onto a white skincare bottle.
Subtle tonal layering, refined typography, understated sophistication and intelligent visual restraint are all encouraged.
Many thanks again and we are very excited to see the next round of directions develop.

```html
<!DOCTYPE html>
<html lang="en">
<head>
<meta charset="utf-8">
<title>Velorique – Light Moisturising Day Cream Packaging</title>
<link href="https://fonts.googleapis.com/css2?family=Marcellus&family=Archivo:wght@400;600&family=Carlito:wght@400;700&display=swap" rel="stylesheet">
<style>
  :root {
    --backdrop: #dddddb;
    --ivory: #f4efe3;
    --plum: #7b3550;
    --charcoal: #1f1c1c;
    --text-grey: #3a3636;
    --blush: #e9d3c8;
    --sand: #b59a7a;
  }
  html, body {
    margin: 0;
    padding: 0;
    width: 1100px;
    height: 1200px;
    overflow: hidden;
    background: var(--backdrop);
  }
  .stage {
    position: relative;
    width: 1100px;
    height: 1200px;
  }
  .panel {
    position: absolute;
    background: var(--ivory);
    overflow: hidden;
  }
  .bottle-label { left: 285px; top: 443px; width: 186px; height: 676px; }
  .carton-front { left: 560px; top: 174px; width: 268px; height: 945px; }

  .wordmark {
    position: absolute;
    font-family: "Marcellus", serif;
    color: var(--charcoal);
    writing-mode: vertical-rl;
    transform: rotate(180deg);
    line-height: 1;
    white-space: nowrap;
  }
  .bottle-label .wordmark { left: -6px; top: 44px; font-size: 74px; }
  .carton-front .wordmark { left: 12px; top: 52px; font-size: 104px; }

  .brand-dot {
    position: absolute;
    border-radius: 50%;
    background: radial-gradient(circle at 50% 45%, #f3e2d8 0%, var(--blush) 55%, #cdb39c 100%);
    border: 1.5px solid var(--sand);
  }
  .bottle-label .brand-dot { left: 75px; top: 42px; width: 64px; height: 64px; }
  .carton-front .brand-dot { left: 143px; top: 46px; width: 96px; height: 96px; }

  .name-band {
    position: absolute;
    left: 0; right: 0;
    background: var(--plum);
    color: var(--ivory);
    font-family: "Archivo", sans-serif;
  }
  .name-band .descriptor { display: block; font-weight: 400; letter-spacing: 0.02em; }
  .name-band .product { display: block; font-weight: 600; letter-spacing: 0.01em; line-height: 1; }
  .bottle-label .name-band { top: 421px; height: 75px; padding-left: 12px; box-sizing: border-box; padding-top: 16px; }
  .bottle-label .descriptor { font-size: 15px; }
  .bottle-label .product { font-size: 27px; margin-top: 4px; }
  .carton-front .name-band { top: 604px; height: 95px; padding-left: 16px; box-sizing: border-box; padding-top: 20px; }
  .carton-front .descriptor { font-size: 20px; }
  .carton-front .product { font-size: 35px; margin-top: 6px; }

  .claims {
    position: absolute;
    font-family: "Carlito", sans-serif;
    color: var(--text-grey);
  }
  .claims .tagline { color: var(--plum); font-weight: 700; margin: 0; }
  .claims .benefit { margin: 0; }
  .bottle-label .claims { left: 12px; top: 507px; }
  .bottle-label .tagline { font-size: 11.5px; }
  .bottle-label .benefit { font-size: 11px; line-height: 15px; margin-top: 3px; }
  .carton-front .claims { left: 16px; top: 712px; }
  .carton-front .tagline { font-size: 14px; }
  .carton-front .benefit { font-size: 14px; line-height: 18px; margin-top: 4px; }

  .attributes {
    position: absolute;
    display: flex;
    font-family: "Carlito", sans-serif;
    color: var(--text-grey);
    text-align: center;
  }
  .attribute { display: flex; flex-direction: column; align-items: center; }
  .attribute svg { display: block; }
  .attribute span { line-height: 1.05; }
  .bottle-label .attributes { left: 12px; top: 584px; gap: 8px; }
  .bottle-label .attribute { width: 28px; }
  .bottle-label .attribute svg { width: 22px; height: 22px; }
  .bottle-label .attribute span { font-size: 6.5px; margin-top: 4px; }
  .carton-front .attributes { left: 14px; top: 792px; gap: 10px; }
  .carton-front .attribute { width: 46px; }
  .carton-front .attribute svg { width: 30px; height: 30px; }
  .carton-front .attribute span { font-size: 10px; margin-top: 6px; }

  .volume {
    position: absolute;
    font-family: "Carlito", sans-serif;
    font-weight: 700;
    color: var(--charcoal);
    margin: 0;
  }
  .bottle-label .volume { left: 13px; top: 639px; font-size: 11.5px; }
  .carton-front .volume { left: 16px; top: 886px; font-size: 16px; }
</style>
</head>
<body>
<div class="stage">

  <section class="panel bottle-label" aria-label="Bottle label">
    <div class="wordmark">velorique</div>
    <div class="brand-dot"></div>
    <div class="name-band">
      <span class="descriptor">LIGHT MOISTURISING</span>
      <span class="product">DAY CREAM</span>
    </div>
    <div class="claims">
      <p class="tagline">Climate Adapt Hydration</p>
      <p class="benefit">Lightweight daily hydration for<br>calm, comfortable skin</p>
    </div>
    <div class="attributes">
      <div class="attribute">
        <svg viewBox="0 0 30 30"><ellipse cx="15" cy="15" rx="14" ry="11" fill="none" stroke="currentColor" stroke-width="1.2"/></svg>
        <span>Terra<br>Natural</span>
      </div>
      <div class="attribute">
        <svg viewBox="0 0 30 30" fill="none" stroke="currentColor" stroke-width="1.2"><path d="M15 3 C6 10 6 21 15 27 C24 21 24 10 15 3 Z"/><path d="M15 8 V27 M15 13 l-4 -3 M15 13 l4 -3 M15 18 l-5 -3 M15 18 l5 -3"/></svg>
        <span>Vegan<br>Friendly</span>
      </div>
      <div class="attribute">
        <svg viewBox="0 0 30 30" fill="none" stroke="currentColor" stroke-width="1.2"><path d="M15 27 V8"/><path d="M15 4 C12 7 12 11 15 13 C18 11 18 7 15 4 Z"/><path d="M15 20 C11 20 6 18 5 13 C10 13 14 15 15 20 Z"/><path d="M15 20 C19 20 24 18 25 13 C20 13 16 15 15 20 Z"/></svg>
        <span>Gluten<br>Free</span>
      </div>
      <div class="attribute">
        <svg viewBox="0 0 30 30" fill="none" stroke="currentColor" stroke-width="1.2"><path d="M15 3 V7"/><path d="M5 13 C5 8 25 8 25 13 Z"/><path d="M7 13 C7 21 11 26 15 27 C19 26 23 21 23 13"/></svg>
        <span>Nut<br>Free</span>
      </div>
    </div>
    <p class="volume">50 ml / 1.69 fl. oz.</p>
  </section>

  <section class="panel carton-front" aria-label="Carton front panel">
    <div class="wordmark">velorique</div>
    <div class="brand-dot"></div>
    <div class="name-band">
      <span class="descriptor">LIGHT MOISTURISING</span>
      <span class="product">DAY CREAM</span>
    </div>
    <div class="claims">
      <p class="tagline">Climate Adapt Hydration</p>
      <p class="benefit">Lightweight daily hydration for<br>calm, comfortable skin</p>
    </div>
    <div class="attributes">
      <div class="attribute">
        <svg viewBox="0 0 30 30"><ellipse cx="15" cy="15" rx="14" ry="11" fill="none" stroke="currentColor" stroke-width="1.2"/></svg>
        <span>Terra<br>Natural</span>
      </div>
      <div class="attribute">
        <svg viewBox="0 0 30 30" fill="none" stroke="currentColor" stroke-width="1.2"><path d="M15 3 C6 10 6 21 15 27 C24 21 24 10 15 3 Z"/><path d="M15 8 V27 M15 13 l-4 -3 M15 13 l4 -3 M15 18 l-5 -3 M15 18 l5 -3"/></svg>
        <span>Vegan<br>Friendly</span>
      </div>
      <div class="attribute">
        <svg viewBox="0 0 30 30" fill="none" stroke="currentColor" stroke-width="1.2"><path d="M15 27 V8"/><path d="M15 4 C12 7 12 11 15 13 C18 11 18 7 15 4 Z"/><path d="M15 20 C11 20 6 18 5 13 C10 13 14 15 15 20 Z"/><path d="M15 20 C19 20 24 18 25 13 C20 13 16 15 15 20 Z"/></svg>
        <span>Gluten<br>Free</span>
      </div>
      <div class="attribute">
        <svg viewBox="0 0 30 30" fill="none" stroke="currentColor" stroke-width="1.2"><path d="M15 3 V7"/><path d="M5 13 C5 8 25 8 25 13 Z"/><path d="M7 13 C7 21 11 26 15 27 C19 26 23 21 23 13"/></svg>
        <span>Nut<br>Free</span>
      </div>
    </div>
    <p class="volume">50 ml / 1.69 fl. oz.</p>
  </section>

</div>
</body>
</html>
```